ALL TEXT GRAPHICS RK May 2025 for Instagram

We are looking for a series of social media graphics for Instagram (new size: 4:5 (1080 x 1350 pixels) ratio that are ALL TEXT. We want the following quotes below on each graphic; one quote per graphic. AND, In very small letters at the bottom of each graphic, add @RKBexleyOnline
The look and feel of these graphics should be complimentary to the color palette attached below; but keep them simple. But the design is up to you; at the end of this document, I provided various samples of all text graphics that I like as examples.
women looking to lose weight

```html
<!DOCTYPE html>
<html lang="en">
<head>
<meta charset="UTF-8">
<title>Tired. Moody. Stubborn Belly Fat.</title>
<link rel="stylesheet" href="https://fonts.googleapis.com/css2?family=DM+Serif+Display&family=Poppins:wght@400;600;700&family=Dancing+Script:wght@500&display=swap">
<style>
  :root {
    --paper: #ffffff;
    --pink-light: #ff73bf;
    --pink-hot: #ff0587;
    --magenta: #d4006b;
    --ink: #000000;
  }
  html, body {
    margin: 0;
    padding: 0;
    overflow: hidden;
    background: var(--paper);
  }
  .post {
    position: relative;
    width: 960px;
    height: 1200px;
    overflow: hidden;
    background: var(--paper);
  }
  .post-frame {
    position: absolute;
    inset: 0;
  }
  .headline {
    position: absolute;
    inset: 0;
  }
  .headline text {
    font-family: "DM Serif Display", Georgia, serif;
    font-size: 172px;
    letter-spacing: -5px;
  }
  .headline .word-tired { fill: var(--pink-light); }
  .headline .word-moody { fill: var(--pink-hot); }
  .headline .word-stubborn { fill: var(--magenta); }
  .headline .word-belly { fill: var(--ink); }
  .subline {
    position: absolute;
    left: 0;
    width: 960px;
    top: 728px;
    margin: 0;
    text-align: center;
    font-family: "Poppins", Arial, sans-serif;
    font-weight: 400;
    font-size: 43px;
    line-height: 58px;
    color: var(--ink);
    padding-left: 26px;
    box-sizing: border-box;
  }
  .subline strong { font-weight: 700; }
  .cta-band {
    position: absolute;
    left: 38px;
    top: 868px;
    width: 884px;
    height: 153px;
    background: var(--magenta);
    display: flex;
    align-items: center;
    justify-content: center;
  }
  .cta-band p {
    margin: 0;
    font-family: "Poppins", Arial, sans-serif;
    font-weight: 700;
    font-size: 74px;
    color: var(--paper);
    letter-spacing: 0;
    padding-top: 6px;
  }
  .handle {
    position: absolute;
    left: 0;
    width: 960px;
    top: 1056px;
    margin: 0;
    text-align: center;
    font-family: "Dancing Script", cursive;
    font-weight: 500;
    font-size: 36px;
    color: var(--ink);
  }
</style>
</head>
<body>
  <main class="post">
    <svg class="post-frame" width="960" height="1200" viewBox="0 0 960 1200" aria-hidden="true">
      <path d="M60 39 H900 A22 22 0 0 0 922 61 V1140 A22 22 0 0 0 900 1162 H60 A22 22 0 0 0 38 1140 V61 A22 22 0 0 0 60 39 Z"
            fill="none" stroke="#d4006b" stroke-width="3"/>
    </svg>

    <svg class="headline" width="960" height="1200" viewBox="0 0 960 1200" role="heading" aria-level="1">
      <text class="word-tired" x="100" y="220">Tired.</text>
      <text class="word-moody" x="100" y="370">Moody.</text>
      <text class="word-stubborn" x="100" y="520">Stubborn</text>
      <text class="word-belly" x="100" y="660">Belly Fat.</text>
    </svg>

    <p class="subline">YOUR <strong>HORMONES</strong> ARE<br>SCREAMING FOR HELP!</p>

    <div class="cta-band">
      <p>LET'S FIX THAT!</p>
    </div>

    <p class="handle">@RKBexleyOnline</p>
  </main>
</body>
</html>
```